A boutique/architectural website for a landscape company

I'm after a minimilstic boutique website for my landscape design and construction business. I have been exploring Wix and created some pages on that but want something more aesthetic.

Industry/Entity Type

Landscaping design and construction

Number of Pages Required

5+ page

Font styles to use
Sans Serif

Colors

Designer to choose colors to be used in the design.

Requirements
Must have
• an architectural, minimalistic look
Nice to have
• Simplicitly and nice images
Should not have
• A corporate look

```html
<!DOCTYPE html>
<html lang="en">
<head>
<meta charset="utf-8">
<title>Linden Landscaping + Design</title>
<link href="https://fonts.googleapis.com/css2?family=Montserrat:wght@400;500;600;700;800&family=Arimo:ital,wght@0,400;1,400&display=swap" rel="stylesheet">
<style>
:root{
  --forest:#073a32;
  --forest-mid:#0c4a3c;
  --sage:#a7bca1;
  --sage-soft:#b9cbb3;
  --ink:#1c1c1c;
  --night:#1b1b1b;
  --white:#ffffff;
  --muted:#d7e1d3;
  --grass-a:#3f6b2c;
  --grass-b:#6f9a43;
}
*{margin:0;padding:0;box-sizing:border-box}
html,body{width:1200px;height:4176px;overflow:hidden;background:var(--white)}
body{position:relative;font-family:'Arimo',Arial,sans-serif;color:var(--ink)}
.abs{position:absolute}
.bg-shapes{position:absolute;left:0;top:0;width:1200px;height:4176px}

/* header */
.site-header{position:absolute;left:0;top:0;width:1200px;height:151px;background:var(--forest);border-bottom:1px solid #5d7d72}
.brand{position:absolute;left:108px;top:40px;width:160px;text-align:center;color:var(--white);font-family:'Montserrat',sans-serif}
.brand-mark{display:inline-block;width:34px;height:34px;border:2px solid var(--white);border-radius:50%;margin-bottom:8px}
.brand-name{font-size:24px;font-weight:400;letter-spacing:8px}
.brand-tag{font-size:7px;letter-spacing:3px;margin-top:4px}
.main-nav{position:absolute;top:72px;left:400px;display:flex;gap:0}
.main-nav a{font-family:'Montserrat',sans-serif;font-size:14px;font-weight:500;color:var(--white);text-decoration:none;position:absolute;white-space:nowrap}
.main-nav a.active{color:#c9d6c4}

/* hero */
.hero-title{position:absolute;top:385px;left:0;width:1200px;text-align:center;color:var(--white);font-family:'Montserrat',sans-serif;font-weight:800;font-size:80px;letter-spacing:1px;line-height:1}
.hero-sub{position:absolute;top:480px;left:0;width:1200px;text-align:center;color:var(--white);font-family:'Montserrat',sans-serif;font-weight:500;font-size:52px;line-height:1}
.btn-pill{position:absolute;display:flex;align-items:center;justify-content:center;border-radius:40px;font-family:'Montserrat',sans-serif;font-weight:600;text-decoration:none}
.hero-btn{left:501px;top:562px;width:198px;height:62px;background:var(--sage);color:var(--white);font-size:18px}

/* section headings */
.section-title{position:absolute;left:0;width:1200px;text-align:center;font-family:'Montserrat',sans-serif;font-weight:700;font-size:41px;color:var(--forest)}
.section-lead{position:absolute;left:0;width:1200px;text-align:center;font-size:15.5px;color:#333}

/* services */
.service-card{position:absolute;top:1092px;width:316px;height:494px;color:var(--white);text-align:center}
.service-card.dark{background:var(--forest)}
.service-card.light{background:var(--sage)}
.service-photo{position:absolute;left:0;top:0;width:316px;height:233px}
.service-icon{position:absolute;left:109px;top:184px;width:98px;height:98px;border-radius:50%}
.service-card.dark .service-icon{background:var(--forest)}
.service-card.light .service-icon{background:var(--sage)}
.service-icon svg{position:absolute;left:29px;top:18px}
.service-name{position:absolute;top:270px;left:0;width:316px;font-family:'Montserrat',sans-serif;font-weight:600;font-size:22px}
.service-text{position:absolute;top:314px;left:20px;width:276px;font-size:13.5px;line-height:26px}
.service-btn{position:absolute;left:90px;top:413px;width:136px;height:48px;border:1.5px solid var(--white);border-radius:30px;display:flex;align-items:center;justify-content:center;font-family:'Montserrat',sans-serif;font-weight:600;font-size:14px;color:var(--white)}

/* about */
.about-wordmark{position:absolute;left:154px;top:1930px;width:420px;text-align:center;font-family:'Montserrat',sans-serif;font-weight:700;font-size:96px;color:var(--white);letter-spacing:6px}
.about-title{position:absolute;left:610px;top:1840px;font-family:'Montserrat',sans-serif;font-weight:700;font-size:41px;color:var(--white)}
.rule{position:absolute;height:3px;width:52px;background:var(--white)}
.about-text{position:absolute;left:610px;top:1918px;width:423px;font-size:13.5px;line-height:26px;color:var(--white);text-align:justify}
.about-btn{left:611px;top:2157px;width:164px;height:56px;background:var(--forest);color:var(--white);font-size:15px}

/* projects */
.project-tile{position:absolute;width:316px}

/* testimonial */
.client-photo{position:absolute;left:146px;top:3323px;width:354px;height:354px;border-radius:50%}
.testi-title{position:absolute;left:561px;top:3336px;font-family:'Montserrat',sans-serif;font-weight:700;font-size:41px;color:var(--white)}
.testi-quote{position:absolute;left:594px;top:3428px;width:466px;font-style:italic;font-size:15px;line-height:26px;color:var(--white);text-align:justify}
.quote-mark{position:absolute;font-family:Georgia,serif;font-weight:700;color:var(--white);font-size:44px;line-height:1}
.testi-name{position:absolute;left:594px;top:3620px;font-family:'Montserrat',sans-serif;font-weight:600;font-size:21px;color:var(--white)}
.stars{position:absolute;left:593px;top:3653px;color:var(--white);font-size:17px;letter-spacing:1px}

/* footer */
.footer-brand{position:absolute;left:176px;top:3905px;width:200px;text-align:center;font-family:'Montserrat',sans-serif;font-weight:500;font-size:34px;letter-spacing:6px;color:var(--white)}
.footer-brand .brand-mark{width:40px;height:40px;display:block;margin:0 auto 12px}
.social{position:absolute;top:4045px;width:36px;height:36px;border:1.5px solid var(--white);border-radius:50%}
.copyright{position:absolute;left:96px;top:4095px;width:360px;text-align:center;font-size:15px;color:var(--white)}
.footer-heading{position:absolute;top:3868px;font-family:'Montserrat',sans-serif;font-weight:400;font-size:21px;color:var(--white)}
.contact-line{position:absolute;left:498px;font-size:14.5px;line-height:22px;color:var(--white);letter-spacing:.5px}
.contact-icon{position:absolute;left:457px}
.signup-text{position:absolute;left:751px;top:3918px;width:330px;font-size:13.5px;line-height:24px;color:var(--white)}
.email-field{position:absolute;left:751px;top:3990px;width:324px;height:42px;background:var(--white);border:1px solid #ccc;border-radius:3px;padding-left:18px;display:flex;align-items:center;font-size:14px;color:#444}
.subscribe-btn{position:absolute;left:751px;top:4047px;width:127px;height:44px;background:var(--forest);color:var(--white);display:flex;align-items:center;justify-content:center;font-family:'Montserrat',sans-serif;font-weight:600;font-size:13px}
</style>
</head>
<body>

<svg class="bg-shapes" width="1200" height="4176" viewBox="0 0 1200 4176" aria-hidden="true">
  <defs>
    <linearGradient id="heroGrad" x1="0" y1="0" x2="1" y2="1">
      <stop offset="0" stop-color="#2f4f2a"/>
      <stop offset=".45" stop-color="#4f7a33"/>
      <stop offset=".75" stop-color="#7c8a72"/>
      <stop offset="1" stop-color="#6a9a3a"/>
    </linearGradient>
  </defs>
  <!-- hero -->
  <path d="M0 740 V762 Q600 1078 1200 758 V740 Z" fill="#0a2e28"/>
  <path d="M0 151 H1200 V750 Q600 1060 0 754 Z" fill="url(#heroGrad)"/>
  <!-- about band -->
  <path d="M0 1780 Q600 1590 1200 1760 V2215 Q600 2470 0 2232 Z" fill="var(--forest)"/>
  <path d="M0 1800 Q600 1610 1200 1772 V2222 Q600 2410 0 2226 Z" fill="var(--sage)"/>
  <!-- footer ground -->
  <rect x="0" y="3620" width="1200" height="556" fill="var(--night)"/>
  <!-- testimonial band -->
  <path d="M0 3290 Q600 3110 1200 3255 V3688 Q600 3935 0 3700 Z" fill="var(--sage-soft)"/>
  <path d="M0 3298 Q600 3122 1200 3264 V3680 Q600 3920 0 3688 Z" fill="var(--forest-mid)"/>
</svg>

<header class="site-header">
  <div class="brand">
    <span class="brand-mark"></span>
    <div class="brand-name">LINDEN</div>
    <div class="brand-tag">LANDSCAPING + DESIGN</div>
  </div>
  <nav class="main-nav">
    <a class="active" href="#" style="left:0">HOME</a>
    <a href="#" style="left:100px">ABOUT US</a>
    <a href="#" style="left:230px">SERVICES</a>
    <a href="#" style="left:359px">PROJECTS</a>
    <a href="#" style="left:494px">NEWS</a>
    <a href="#" style="left:594px">CONTACT US</a>
  </nav>
</header>

<div class="abs" role="img" aria-label="Photo of a terraced garden with curved stone retaining walls, shrubs and lawn" style="left:0;top:151px;width:1200px;height:600px"></div>
<h1 class="hero-title">LINDEN</h1>
<p class="hero-sub">LANDSCAPING. DESIGN</p>
<a class="btn-pill hero-btn" href="#">READ MORE</a>

<h2 class="section-title" style="top:966px">OUR SERVICES</h2>
<p class="section-lead" style="top:1028px">Sed ut perspiciatis unde omnis iste natus error sit voluptatem accusantium doloremque laudantium</p>

<article class="service-card dark" style="left:112px">
  <div class="service-photo" role="img" aria-label="Photo of a gardener mowing a lawn" style="background:linear-gradient(160deg,#2d4a22,#5c8a34 55%,#7aa648)"></div>
  <div class="service-icon"><svg width="40" height="40" viewBox="0 0 40 40" fill="none" stroke="#fff" stroke-width="2"><path d="M4 12v24M12 12v24M20 12v24M28 12v24M36 12v24M2 18h36M2 30h36"/></svg></div>
  <h3 class="service-name">Lawn &amp; Garden Care</h3>
  <p class="service-text">Sed ut perspiciatis unde omnis iste natus error sit voluptatem accusantium doloremque laudantium, totam rem aperiam,</p>
  <a class="service-btn" href="#">READ MORE</a>
</article>
<article class="service-card light" style="left:443px">
  <div class="service-photo" role="img" aria-label="Photo of curved stone garden beds with planting" style="background:linear-gradient(170deg,#3c5e2e,#5f8a3e 55%,#a89a7a)"></div>
  <div class="service-icon"><svg width="40" height="40" viewBox="0 0 40 40" fill="none" stroke="#fff" stroke-width="2"><circle cx="13" cy="12" r="8"/><circle cx="27" cy="12" r="8"/><path d="M13 20v8M27 20v8M6 28h28v8H6z"/></svg></div>
  <h3 class="service-name">Landscaping</h3>
  <p class="service-text">Sed ut perspiciatis unde omnis iste natus error sit voluptatem accusantium doloremque laudantium, totam rem aperiam,</p>
  <a class="service-btn" href="#">READ MORE</a>
</article>
<article class="service-card dark" style="left:774px">
  <div class="service-photo" role="img" aria-label="Photo of a gardener pruning a hedge with shears" style="background:linear-gradient(150deg,#4c6e2c,#a58e6c 50%,#3d5e26)"></div>
  <div class="service-icon"><svg width="40" height="40" viewBox="0 0 40 40" fill="none" stroke="#fff" stroke-width="2"><path d="M14 2l8 20M26 2l-8 20"/><circle cx="14" cy="30" r="6"/><circle cx="26" cy="30" r="6"/></svg></div>
  <h3 class="service-name">Pruning plants</h3>
  <p class="service-text">Sed ut perspiciatis unde omnis iste natus error sit voluptatem accusantium doloremque laudantium, totam rem aperiam,</p>
  <a class="service-btn" href="#">READ MORE</a>
</article>

<div class="about-wordmark">LINDEN</div>
<h2 class="about-title">ABOUT US</h2>
<span class="rule" style="left:610px;top:1896px"></span>
<p class="about-text">Sed ut perspiciatis unde omnis iste natus error sit voluptatem accusantium doloremque laudantium, totam rem aperiam, eaque ipsa quae ab illo inventore veritatis et quasi architecto beatae vitae dicta sunt explicabo. Nemo enim ipsam voluptatem quia voluptas sit aspernatur aut odit aut fugit, sed quia consequuntur magni dolores eos qui ratione voluptatem sequi nesciunt. Neque porro quisquam est, qui dolorem ipsum quia dolor sit amet, consectetur, adipisci velit, sed quia non aliquam quaerat voluptatem.</p>
<a class="btn-pill about-btn" href="#">READ MORE</a>

<h2 class="section-title" style="top:2410px">RECENT PROJECTS</h2>
<p class="section-lead" style="top:2474px">Sed ut perspiciatis unde omnis iste natus error sit voluptatem accusantium doloremque laudantium</p>

<div class="project-tile" role="img" aria-label="Photo of a planted bed with hostas and flowering shrubs" style="left:112px;top:2538px;height:280px;background:linear-gradient(160deg,#5a4038,#4d7a33 55%,#78a646)"></div>
<div class="project-tile" role="img" aria-label="Photo of a garden with a curved stone wall and lawn" style="left:443px;top:2538px;height:280px;background:linear-gradient(170deg,#4a7a34,#6d9a3e 60%,#8fbf4a)"></div>
<div class="project-tile" role="img" aria-label="Photo of a house front with colourful flowering shrubs" style="left:774px;top:2538px;height:280px;background:linear-gradient(180deg,#6e9fd0,#b5a89a 45%,#c24a6e 70%,#6aa03c)"></div>
<div class="project-tile" role="img" aria-label="Aerial photo of a backyard garden with paths and planting" style="left:112px;top:2834px;height:277px;background:linear-gradient(160deg,#6a8a3a,#8cb84a 55%,#5b7a33)"></div>
<div class="project-tile" role="img" aria-label="Aerial photo of a winding paved garden path through lawn" style="left:443px;top:2834px;height:277px;background:linear-gradient(150deg,#3e6a24,#5c8c30 55%,#b59a78)"></div>
<div class="project-tile" role="img" aria-label="Photo of stone garden steps lined with flowers" style="left:774px;top:2834px;height:277px;background:linear-gradient(165deg,#6a6a55,#d6c24a 35%,#7a6a9a 55%,#a0896a)"></div>

<div class="client-photo" role="img" aria-label="Photo of a smiling gardener holding a crate of seedlings" style="background:radial-gradient(circle at 50% 45%,#9a7a5a,#5a6a3a 60%,#2f4a2a)"></div>
<h2 class="testi-title">TESTIMONIALS</h2>
<span class="rule" style="left:561px;top:3398px"></span>
<span class="quote-mark" style="left:560px;top:3428px">&ldquo;</span>
<p class="testi-quote">Sed ut perspiciatis unde omnis iste natus error sit voluptatem accusantium doloremque laudantium, totam rem aperiam, eaque ipsa quae ab illo inventore veritatis et quasi architecto beatae vitae dicta sunt explicabo. Nemo enim ipsam voluptatem quia voluptas sit aspernatur aut odit aut fugit, sed quia consequuntur magni dolores eos qui ratione voluptatem sequi nesciunt. Neque porro quisquam dolore magnam aliquam quaerat voluptatem.</p>
<span class="quote-mark" style="left:904px;top:3585px">&rdquo;</span>
<p class="testi-name">Elias Marrow</p>
<p class="stars">★★★★★</p>

<footer>
  <div class="footer-brand"><span class="brand-mark"></span>LINDEN</div>
  <span class="social" style="left:170px"></span>
  <span class="social" style="left:214px"></span>
  <span class="social" style="left:258px"></span>
  <span class="social" style="left:302px"></span>
  <p class="copyright">Copyright © 2021. All rights reserved.</p>

  <h4 class="footer-heading" style="left:457px">CONTACT US</h4>
  <svg class="contact-icon" style="top:3932px" width="20" height="24" viewBox="0 0 20 24" fill="none" stroke="#fff" stroke-width="1.5"><path d="M10 23s8-8 8-13a8 8 0 0 0-16 0c0 5 8 13 8 13z"/><circle cx="10" cy="10" r="3"/></svg>
  <p class="contact-line" style="top:3922px">Address :<br>265 orem Ipsum Dummy<br>Lorem Ipsum</p>
  <svg class="contact-icon" style="top:4008px" width="20" height="20" viewBox="0 0 20 20" fill="none" stroke="#fff" stroke-width="1.5"><path d="M4 1l4 4-2 3c1 3 3 5 6 6l3-2 4 4-3 3C8 19 1 12 1 4z"/></svg>
  <p class="contact-line" style="top:4005px">Phone :<br>000.555.0142</p>
  <svg class="contact-icon" style="top:4079px" width="22" height="16" viewBox="0 0 22 16" fill="none" stroke="#fff" stroke-width="1.5"><rect x="1" y="1" width="20" height="14"/><path d="M1 1l10 8 10-8"/></svg>
  <p class="contact-line" style="top:4076px">Email :<br>hello@lindenyard.com</p>

  <h4 class="footer-heading" style="left:751px">SIGN UP TO RECEIVE EMAIL</h4>
  <p class="signup-text">Excepteur sint occaecat cupidatat non proident, sunt in culpa qui nemo enim ipsam</p>
  <div class="email-field">Enter Email</div>
  <div class="subscribe-btn">SUBSCRIBE</div>
</footer>

</body>
</html>
```